Business card for Bright Keystone

Front (space for each) - Name, title, qualifications, mobile number, email address, website, name/logo,
Back - Business name/logo and slogan "your dream is our vision" underneath,
in small writing underneath need ABN number, CRN number, ACL number
Target Market(s)
First Home Buyers
Industry/Entity Type
Finance
Contact Information for Business Card
Requirements
Must have
- Front (space for each) - Name, title, qualifications, mobile number, email address, website, name/logo,

```html
<!DOCTYPE html>
<html lang="en">
<head>
<meta charset="utf-8">
<title>Bright Keystone — Business Card</title>
<link rel="stylesheet" href="https://fonts.googleapis.com/css2?family=Montserrat:wght@600;800&family=Arimo:wght@400&display=swap">
<style>
  :root {
    --canvas-bg: #2b2b2b;
    --teal: #00aaad;
    --teal-mid: #1db49a;
    --green: #8dc63f;
    --ink: #111111;
    --text: #1e1e1e;
    --divider: #c9c9c9;
    --white: #ffffff;
  }
  * { margin: 0; padding: 0; box-sizing: border-box; }
  html, body { width: 1200px; height: 1015px; overflow: hidden; }
  body {
    background: var(--canvas-bg);
    font-family: "Arimo", Arial, sans-serif;
    position: relative;
  }
  .card {
    position: absolute;
    left: 250px;
    width: 700px;
    height: 400px;
    overflow: hidden;
    box-shadow: 0 14px 30px rgba(0,0,0,0.45);
  }
  /* Back side */
  .card--back { top: 55px; }
  .card-back__pattern {
    position: absolute; inset: 0;
    background: linear-gradient(180deg, var(--green) 0%, var(--teal-mid) 55%, var(--teal) 100%);
  }
  .card-back__name {
    position: absolute; inset: 0;
    display: flex; align-items: center; justify-content: center;
    font-family: "Montserrat", sans-serif;
    font-weight: 600;
    font-size: 28px;
    color: var(--white);
  }
  /* Front side */
  .card--front { top: 520px; background: var(--white); }
  .brand {
    position: absolute; left: 60px; top: 124px;
    width: 300px;
    font-family: "Montserrat", sans-serif;
    font-weight: 600;
    font-size: 30px;
    line-height: 1.2;
    color: var(--ink);
    white-space: nowrap;
  }
  .divider {
    position: absolute; left: 385px; top: 40px;
    width: 1px; height: 205px; background: var(--divider);
  }
  .contact { position: absolute; left: 410px; top: 58px; }
  .contact__name {
    font-family: "Montserrat", sans-serif;
    font-weight: 800; font-size: 22px; letter-spacing: 0.5px;
    color: var(--teal-mid); text-transform: uppercase;
  }
  .contact__title { font-size: 15px; color: var(--text); margin-top: 2px; }
  .contact__list { list-style: none; margin-top: 22px; }
  .contact__list li {
    display: flex; align-items: center; gap: 10px;
    font-size: 15px; color: var(--text); margin-bottom: 7px;
  }
  .contact__list svg { width: 20px; height: 20px; flex: none; }
  .band { position: absolute; left: 0; top: 0; width: 700px; height: 400px; }
  .slogan {
    position: absolute; right: 40px; bottom: 36px; text-align: right; color: var(--white);
  }
  .slogan__line {
    font-family: "Montserrat", sans-serif; font-weight: 800;
    font-size: 25px; letter-spacing: 0.5px; text-transform: uppercase;
  }
  .slogan__ids { font-size: 13px; margin-top: 3px; letter-spacing: 0.3px; }
</style>
</head>
<body>

<section class="card card--back" aria-label="Card back">
  <div class="card-back__pattern" role="img" aria-label="Repeating light decorative pattern over a green to teal gradient"></div>
  <div class="card-back__name">Bright Keystone</div>
</section>

<section class="card card--front" aria-label="Card front">
  <svg class="band" viewBox="0 0 700 400" aria-hidden="true">
    <defs>
      <linearGradient id="bandGradient" x1="0" y1="1" x2="1" y2="0">
        <stop offset="0" stop-color="#00aaad"/>
        <stop offset="0.55" stop-color="#2bb88f"/>
        <stop offset="1" stop-color="#8dc63f"/>
      </linearGradient>
    </defs>
    <polygon points="0,318 700,262 700,400 0,400" fill="url(#bandGradient)"/>
  </svg>

  <div class="brand">Bright Keystone</div>

  <div class="divider"></div>

  <div class="contact">
    <div class="contact__name">Daniel Hargrove</div>
    <div class="contact__title">Managing Director</div>
    <ul class="contact__list">
      <li>
        <svg viewBox="0 0 20 20"><circle cx="10" cy="10" r="10" fill="#1db49a"/><path d="M7 5.5l1.6 2.2-1 1.2a6 6 0 0 0 3.5 3.5l1.2-1 2.2 1.6-.8 1.6c-4 .2-7.7-3.5-7.5-7.5z" fill="#fff"/></svg>
        044-987 654 321
      </li>
      <li>
        <svg viewBox="0 0 20 20"><circle cx="10" cy="10" r="10" fill="#1db49a"/><rect x="5" y="6.5" width="10" height="7" fill="#fff"/><path d="M5 6.5l5 4 5-4" fill="none" stroke="#1db49a" stroke-width="1"/></svg>
        hello@brightkeystone.com
      </li>
      <li>
        <svg viewBox="0 0 20 20"><circle cx="10" cy="10" r="10" fill="#1db49a"/><g fill="none" stroke="#fff" stroke-width="1"><circle cx="10" cy="10" r="5"/><ellipse cx="10" cy="10" rx="2.2" ry="5"/><path d="M5 10h10M6 7.5h8M6 12.5h8"/></g></svg>
        www.brightkeystone.com
      </li>
    </ul>
  </div>

  <div class="slogan">
    <div class="slogan__line">Your dream is our vision</div>
    <div class="slogan__ids">ABN 418290 | CRN 507614 | ACL 362758</div>
  </div>
</section>

</body>
</html>
```